Brazilian-Italian food blogger looks for a yummy design for her blog

Ciao everyone! I am looking for a brand new design for my Wordpress food blog, MaReVIA (marevia-example.com). The blog is about my deep love with food and with Bologna. I write particularly for the Brazilian crowd.
I talk about gastronomic curiosities of the town, delicious places and specialties that one can only find here. There are also many posts about my trips around Italy.
I would like the new design to be more sophisticated (or should I say professional?), but friendly at the same time.
If possible, I would like to keep its background very clean (if there are patters related to food, like the way it is now, even better), especially because I post many big colourful photos...
Also, since it is a personal blog, I would love if visitors could see a picture of mine and with a short description right at the homepage.
Thank you so much in advance.
Cheers,
Lidia.

Target Market(s)

Brazilian people interested in Italian culture and gastronomy.

Colors
fcca95

Requirements
Must have
• A neutral background that does not interfere with photos.
• My photo with a short description on the homepage.
Nice to have
• A background that has something to do with food.
Should not have
• It should not look like a girly blog.

```html
<!DOCTYPE html>
<html lang="pt">
<head>
<meta charset="utf-8">
<title>MaReVIA</title>
<link href="https://fonts.googleapis.com/css2?family=Oswald:wght@400;500&family=Open+Sans:wght@400;600&display=swap" rel="stylesheet">
<style>
:root{
  --peach:#fcca95;
  --peach-dark:#f6b777;
  --peach-light:#fde3c6;
  --page:#e3e3e3;
  --panel:#f4f4f4;
  --panel-border:#ead8c8;
  --text:#6b6b6b;
  --title:#333;
  --link:#a8803f;
  --footer:#ece2db;
  --white:#fff;
}
*{box-sizing:border-box;margin:0;padding:0}
html,body{width:1200px;height:2466px;overflow:hidden}
body{position:relative;background:var(--page);font-family:"Open Sans",Arial,sans-serif;color:var(--text);font-size:12.5px;line-height:1.55}
a{color:var(--link)}
.page-pattern{position:absolute;left:0;top:86px;width:1200px;height:2277px;background:linear-gradient(#e6e6e6,#dedede)}
.site-header{position:absolute;left:0;top:0;width:1200px;height:86px;background:linear-gradient(var(--peach-light),var(--peach))}
.logo{position:absolute;left:132px;top:20px;font-family:"Oswald",sans-serif;font-weight:500;font-size:22px;color:#fff;letter-spacing:.5px}
.search{position:absolute;left:884px;top:26px;width:168px;height:22px;background:#e9e9e9;border:1px solid #d6d6d6;font-size:11px;color:#999;padding:2px 8px}
.search-icon{position:absolute;left:1056px;top:28px}
.main-nav{position:absolute;left:191px;top:74px;width:806px;height:42px;background:var(--white);border:3px solid var(--peach-light);display:flex;align-items:center;justify-content:space-around;padding:0 10px;font-size:11.5px;color:#555}
.side-menu{position:absolute;left:138px;top:136px;width:180px;height:337px;background:var(--panel);border:4px solid var(--peach-light);padding:6px 14px;font-family:"Oswald",sans-serif;font-size:12px;color:#555;text-align:center}
.side-menu li{list-style:none;height:40px;line-height:40px;border-bottom:1px dashed #cfcfcf}
.side-menu li:last-child{border:none}
.slider{position:absolute;left:343px;top:136px;width:717px;height:337px;border:4px solid var(--white);background:linear-gradient(#5a6fb8 0%,#8c8fc2 35%,#c25f2e 55%,#8a3a1e 100%)}
.slider-arrow{position:absolute;top:150px;width:22px;height:22px}
.content{position:absolute;left:136px;top:510px;width:657px;height:1829px;background:var(--panel);border:4px solid var(--panel-border);padding:16px 28px 0}
.post{position:relative;height:396px}
.post h2{font-family:"Oswald",sans-serif;font-weight:500;font-size:18px;color:var(--title);margin-top:6px}
.meta{font-size:11px;color:#555;margin:10px 0 16px}
.thumb{float:left;width:156px;height:156px;margin:0 16px 10px 0;border:3px solid #fff;box-shadow:0 0 2px #ccc}
.post p{margin-bottom:10px}
.quote{float:left;clear:left;width:230px;margin:4px 16px 0 0;font-style:italic;font-weight:600;color:#999;font-size:12px}
.read-more{position:absolute;right:0;bottom:14px;width:128px;height:30px;border-radius:15px;background:linear-gradient(var(--peach-light),var(--peach));border:2px solid #fff;box-shadow:0 1px 3px #bbb;font-size:12px;color:#555;text-align:center;line-height:26px}
.pagination{position:absolute;left:526px;top:1770px;display:flex;gap:6px;font-size:11px}
.pagination span{background:#e6e6e6;border:1px solid #d6d6d6;padding:1px 8px}
.sidebar{position:absolute;left:804px;top:510px;width:256px;height:1829px;background:var(--panel);border:4px solid var(--panel-border);padding:10px 14px;font-size:11px}
.sidebar h3{font-family:"Oswald",sans-serif;font-weight:500;font-size:13px;color:var(--title);margin:6px 0 14px}
.about{text-align:center;margin-bottom:40px}
.avatar{display:block;width:66px;height:99px;margin:0 auto 6px;background:linear-gradient(#3b2a40,#7a5a6a)}
.like-box{border:1px solid #ddd;background:#fff;padding:8px;height:180px;margin-bottom:86px}
.like-btn{display:inline-block;width:44px;height:18px;background:#5b74a8;margin-left:6px}
.faces{height:104px;margin-top:8px;background:linear-gradient(90deg,#6a5a55,#a89080,#5e6070)}
.recent li{list-style:none;display:grid;grid-template-columns:66px 62px 1fr;gap:6px;height:123px;font-size:10.5px;line-height:1.4}
.recent .date{text-align:center;font-size:10px;color:#333}
.recent .date b{display:block;font-family:"Oswald",sans-serif;font-weight:400;font-size:24px}
.recent .mini{width:56px;height:56px}
.recent .excerpt{grid-column:1/4;margin-top:-60px;padding-top:0}
.cats li{list-style:none;margin-bottom:14px}
.cats li::before{content:"» ";color:#999}
.site-footer{position:absolute;left:0;top:2363px;width:1200px;height:103px;background:var(--footer);border-top:8px solid var(--peach-dark);font-size:11px;padding:46px 154px}
</style>
</head>
<body>
<div class="page-pattern" role="img" aria-label="Light grey background pattern of forks, knives and spoons"></div>

<header class="site-header">
  <div class="logo">MaReVIA</div>
  <div class="search">Search</div>
  <svg class="search-icon" width="16" height="16" viewBox="0 0 16 16"><circle cx="6.5" cy="6.5" r="4.5" fill="none" stroke="#999" stroke-width="2"/><line x1="10" y1="10" x2="14" y2="14" stroke="#999" stroke-width="2"/></svg>
</header>

<nav class="main-nav">
  <span>Bella Bo</span><span>BUONI POSTI</span><span>CONFISSÕES GASTRONÔMICAS</span><span>Contato</span><span>Eu, Lidia</span><span>MaReVIA</span><span>FUORI CASA</span><span>LISTA DE RESTAURANTES</span><span>O blog</span>
</nav>

<ul class="side-menu">
  <li>Home</li><li>O blog</li><li>Bella Bo</li><li>BUONI POSTI</li><li>Eu, Lidia</li><li>FUORI CASA</li><li>LISTA DE RESTAURANTES</li><li>Contato</li>
</ul>

<div class="slider" role="img" aria-label="Photo of Bologna rooftops and medieval towers at sunset">
  <svg class="slider-arrow" style="left:10px" viewBox="0 0 22 22"><path d="M14 4 L7 11 L14 18" fill="none" stroke="#ddd" stroke-width="2"/></svg>
  <svg class="slider-arrow" style="right:10px" viewBox="0 0 22 22"><path d="M8 4 L15 11 L8 18" fill="none" stroke="#ddd" stroke-width="2"/></svg>
</div>

<main class="content">
  <article class="post">
    <h2>Dando de barato</h2>
    <div class="meta">September 16, 2014, Posted in <a>Pasta</a> | <a>No comments</a> | <a>Edit</a></div>
    <div class="thumb" role="img" aria-label="Plate of pasta" style="background:linear-gradient(#f0c050,#d98a2a)"></div>
    <p>É inquietante como damos de barato certas coisas que, no fundo são excepcionais – e raras. A companhia de pessoas queridas, o litoral brasileiro, água-de-coco… Pequenas coisas que, ainda que muito especiais, por se tornarem corriqueiras nas nossas vidas, não damos o devido valor.</p>
    <p>Me dei conta que um desses exemplos é um dos restaurantes de que mais gosto aqui em Bologna, o <em>Sal Fino</em>.</p>
    <p>Bato ponto pelo menos uma vez por semana – já virou quase rotina – e por me sentir sempre em casa, por conhecer os chefs e os garçons, e, principalmente, porque comer bem ali é uma constância, deixei de perceber que a qualidade dos pratos do local é extraordinária, e muito difícil de se replicada.</p>
    <p>O <em>Sal Fino</em> é um dos raros exemplos de cozinha meridional (i.e...</p>
    <div class="read-more">Read More</div>
  </article>

  <article class="post" style="height:551px">
    <h2>Mortadella Bologna</h2>
    <div class="meta">September 16, 2014, Posted in <a>Uncategorized</a> | <a>No comments</a> | <a>Edit</a></div>
    <div class="thumb" role="img" aria-label="Mortadella and cured meats" style="background:linear-gradient(#c4454a,#e8a0a0)"></div>
    <p>Em uma pequena ruazinha chamada Vicolo dei Girasoli, bem no centro histórico de Bologna, há uma placa, redonda, com os seguintes dizeres:</p>
    <p>Em outras palavras, foi bem ali que a história do embutido cor-de-rosa mais querido do mundo se misturou à de Bologna, a ponto de receber o próprio nome da cidade, <em>"Mortadella Bologna"</em>.</p>
    <p>Os Salumai, mencionados na placa, eram os membros da cooperativa mais antiga de produtores de frios da região, responsáveis pela elaboração de mortadela e outros salumi desde o século XII.</p>
    <div class="quote">“Esta casa era a sede, de 1242 a 1796, da arte dos Salumai, que controlavam a produção dos salumi Bolognesi, dos quais a excelente mortadela fez grande no mundo o mito de Bologna “la grassa” (“a gorda”)”.</div>
    <p>Sua história é peculiar: an...</p>
    <div class="read-more">Read More</div>
  </article>

  <article class="post">
    <h2>Simplesmente pão e leite</h2>
    <div class="meta">September 16, 2014, Posted in <a>Sweets</a> | <a>No comments</a> | <a>Edit</a></div>
    <div class="thumb" role="img" aria-label="Bread and cake on a table" style="background:linear-gradient(#8a5a3a,#d7b08a)"></div>
    <p>No fim de semana passado, escapei (de novo) para a montanha, desta vez para as Dolomitas, no Trentino-Alto Adige. Essa é uma região muito particular da Itália, onde a primeira língua é o alemão, e, de tão organizada e precisa, qualquer italiano vindo de outro lugar se sente um peixe fora d'água.</p>
    <p>Mas, de jeito nenhum digo isso em modo depreciativo; é uma delícia rodar por estradas sem buracos, visitar lugares turísticos (como as trilhas da Marmolada, uma montanha perenemente coberta de neve, ou aquelas que levam ao alto dos 3.152m do Piz Boè) sem se perder no meio do caminho. Sem falar que é muito divertido ouvir as pessoas misturarem o alemão com o italiano sem perceber.</p>
    <p>Porém, confesso foram duas coisas muito simples que mais impressionaram: o pão e o iogurte.</p>
    <p>Isso mesmo.</p>
    <div class="read-more">Read More</div>
  </article>

  <article class="post">
    <h2>Insalata di riso della Giulia</h2>
    <div class="meta">September 16, 2014, Posted in <a>Riso</a> | <a>No comments</a> | <a>Edit</a></div>
    <div class="thumb" role="img" aria-label="Colourful rice salad" style="background:linear-gradient(#f2e2a0,#d9603a)"></div>
    <p>Dizem aqui que toda menina italiana tem sua receita de <em>insalata di riso</em>. Sinceramente não sei quanto seja verdade e, confesso, receita minha mesmo só deixadala di farro (já mostrei <a>aqui</a>). Mas, para me garantir, peguei emprestado a receita da minha sogra e, como funciona tão bem, não pretendo mudar.</p>
    <p>A <em>insalata di riso</em> é muito comum nas mesas italianas, de norte a sul. Mesmo nas lojas que vendem comidas prontas, ela marca presença quase o ano todo.</p>
    <p>Mas o bacana mesmo é que não existe uma receita típica, em cada esquina ela tem uma cara diferente. A única coisa em comum é o fato de ser feita com arroz e essencialmente coisinhas que qualquer um compra já prontas no supermercado: atum, azeitona, ervilhas, queijo, conservas, presunto, salsicha, e por aí vai...</p>
    <div class="read-more">Read More</div>
  </article>

  <div class="pagination"><span>1</span><span>2</span><span>Next »</span></div>
</main>

<aside class="sidebar">
  <h3>About</h3>
  <div class="about">
    <span class="avatar" role="img" aria-label="Portrait photo of the blogger"></span>
    <b>MaReVIA</b><br>Minha declaração de amor ao comer bem e a Bologna
  </div>

  <h3>Like the blog</h3>
  <div class="like-box">
    <div style="display:flex;align-items:center"><span style="width:40px;height:40px;background:#8a6a5a;display:inline-block" role="img" aria-label="Blog profile picture"></span><span style="margin-left:6px">MaReVIA<br><span class="like-btn" style="margin:0"></span></span></div>
    <div style="margin-top:4px">144 people like MaReVIA.</div>
    <div class="faces" role="img" aria-label="Grid of follower profile pictures"></div>
    <div style="font-size:9px;margin-top:4px">Social plugin</div>
  </div>

  <h3>Recent Posts</h3>
  <ul class="recent">
    <li><div class="date"><b>16</b>September</div><div class="mini" role="img" aria-label="Pasta" style="background:#e8a840"></div><div><a>Dando de barato</a><br>É inquietante como damos de barato certas coisas, que, no</div></li>
    <li><div class="date"><b>16</b>September</div><div class="mini" role="img" aria-label="Mortadella" style="background:#c4606a"></div><div><a>Mortadella Bologna</a><br>Em uma pequena ruazinha chamada Vicolo dos</div></li>
    <li><div class="date"><b>16</b>September</div><div class="mini" role="img" aria-label="Bread" style="background:#a67850"></div><div><a>Simplesmente pão e leite</a><br>No fim de semana passado,</div></li>
    <li><div class="date"><b>16</b>September</div><div class="mini" role="img" aria-label="Rice salad" style="background:#e8b070"></div><div><a>Insalata di riso della Giulia</a><br>Dizem aqui que toda menina</div></li>
    <li><div class="date"><b>14</b>September</div><div class="mini" role="img" aria-label="Brazilian dish" style="background:#b88a4a"></div><div><a>Saudades</a><br>Em uma visita pra-trás por São Paulo, me dei conta que, além</div></li>
    <li><div class="date"><b>13</b>September</div><div class="mini" role="img" aria-label="Magic mountain dessert" style="background:#d8a030"></div><div><a>Montanha mágica</a><br>Não sei se é mal de brasileiro, ou só meu mesmo,</div></li>
  </ul>

  <h3 style="margin-top:18px">Categories</h3>
  <ul class="cats">
    <li><a>Mortadella</a></li><li><a>Pasta</a></li><li><a>Riso</a></li><li><a>Sweets</a></li><li><a>Uncategorized</a></li>
  </ul>
</aside>

<footer class="site-footer">Copyright © 2014 <a>MaReVIA</a></footer>
</body>
</html>
```